Banner Designs for Field Keep Ad Campaign

Harrowmere is a security consulting and services company that offers a service called FieldKeepUnit. FieldKeepUnit helps our customers secure large events by providing rapidly deployable security and communications technologies in a Field Keep vehicle, on a per event basis. We are looking for a designer to create a banner ad in three sizes for our campaign.
Target Market(s)
Our campaign is geared to the sports and entertainment industry, specifically large event venues and their security operation.
Industry/Entity Type
Security
Font styles to use
Other font styles liked:
- Raleway
Requirements
Must have
- Banner Objective
The visual and textual content of the banner should prompt the viewer to quickly identify the service offered and the information that is available to download.
Banner Design
Logo: FieldKeepUnit logo
Call to Action Button in Red: Get Details (On Right or or Upper Right)
Title in Larger Font: Take Control of you Events
Subtitle in smaller Font: Your Force Multiplier - Field Keep as a Service
Background: Photo of Field Keep interior or exterior or photo of female operator.
Font: Raleway
Banner Sizes
1 - 1200x670 pixels
2 - 1510x196 pixels
3 - 1200x628 pixels
Nice to have
- Follow the look and feel of the samples provided.

```html
<!DOCTYPE html>
<html lang="en">
<head>
<meta charset="utf-8">
<title>FieldKeepUnit Banner Set</title>
<link rel="stylesheet" href="https://fonts.googleapis.com/css2?family=Raleway:wght@400;500;600;800;900&display=swap">
<style>
  :root {
    --sheet: #ececec;
    --ink-dark: #07090c;
    --title-blue: #2f78c2;
    --white: #ffffff;
    --ribbon-red: #d11a0e;
    --photo-dark: #0c1116;
    --photo-mid: #1c2630;
    --photo-warm: #5a4034;
    --photo-skin: #8a6550;
  }
  * { box-sizing: border-box; margin: 0; padding: 0; }
  html, body {
    width: 1200px; height: 600px; overflow: hidden;
    background: var(--sheet);
    font-family: "Raleway", Arial, sans-serif;
  }
  .sheet { position: relative; width: 1200px; height: 600px; }

  .banner {
    position: absolute; overflow: hidden;
    background: var(--ink-dark);
    box-shadow: 2px 4px 8px rgba(0,0,0,.35);
  }
  .banner--square-a { left: 31px; top: 59px; width: 545px; height: 298px; }
  .banner--square-b { left: 609px; top: 58px; width: 560px; height: 287px; }
  .banner--wide { left: 31px; top: 397px; width: 1138px; height: 145px; }

  .photo { position: absolute; inset: 0; }
  .banner--square-a .photo,
  .banner--square-b .photo {
    background:
      radial-gradient(ellipse 38% 62% at 80% 52%, var(--photo-skin) 0%, var(--photo-warm) 45%, rgba(40,32,28,0) 100%),
      linear-gradient(90deg, var(--photo-dark) 0%, var(--photo-mid) 55%, #2a2622 100%);
  }
  .banner--wide .photo {
    left: 640px;
    background:
      radial-gradient(ellipse 40% 80% at 62% 55%, var(--photo-skin) 0%, var(--photo-warm) 45%, rgba(40,32,28,0) 100%),
      linear-gradient(90deg, var(--ink-dark) 0%, var(--photo-mid) 45%, #2a2622 100%);
  }

  .brand { position: absolute; color: var(--white); }
  .brand__name { display: block; font-weight: 500; line-height: 1; letter-spacing: .2px; }
  .brand__by { display: block; text-align: right; font-weight: 600; line-height: 1; margin-top: 5px; }

  .headline {
    position: absolute; color: var(--title-blue);
    font-weight: 900; text-transform: uppercase; line-height: 1; letter-spacing: 1px;
  }
  .tagline { position: absolute; color: var(--white); font-weight: 500; white-space: nowrap; }

  .banner--square-a .brand { left: 29px; top: 58px; }
  .banner--square-b .brand { left: 29px; top: 49px; }
  .banner--square-a .brand__name, .banner--square-b .brand__name { font-size: 19px; }
  .banner--square-a .brand__by, .banner--square-b .brand__by { font-size: 8px; }

  .banner--square-a .headline { left: 29px; top: 128px; font-size: 33px; line-height: 33px; }
  .banner--square-b .headline { left: 29px; top: 124px; font-size: 33px; line-height: 34px; }
  .banner--square-a .tagline { left: 29px; top: 199px; font-size: 11px; }
  .banner--square-b .tagline { left: 29px; top: 196px; font-size: 11px; }

  .banner--wide .brand { left: 40px; top: 54px; }
  .banner--wide .brand__name { font-size: 20px; }
  .banner--wide .brand__by { font-size: 8px; }
  .banner--wide .headline { left: 258px; top: 41px; font-size: 35px; white-space: nowrap; }
  .banner--wide .tagline { left: 258px; top: 81px; font-size: 18px; }

  .ribbon { position: absolute; inset: 0; width: 100%; height: 100%; }
  .ribbon text {
    font-family: "Raleway", Arial, sans-serif; font-weight: 900;
    fill: var(--white); text-transform: uppercase; letter-spacing: .5px;
  }
</style>
</head>
<body>
<main class="sheet">

  <section class="banner banner--square-a">
    <div class="photo" role="img" aria-label="Photo of a female operator wearing a headset in a dim command centre"></div>
    <div class="brand"><span class="brand__name">FieldKeepUnit</span><span class="brand__by">By Harrowmere</span></div>
    <h1 class="headline">Take Control<br>of Your Events</h1>
    <p class="tagline">Your Force Multiplier - Field Keep as a Service</p>
    <svg class="ribbon" viewBox="0 0 545 298" aria-hidden="true">
      <polygon points="398,0 455,0 545,90 545,147" fill="var(--ribbon-red)"/>
      <text x="0" y="0" font-size="19" text-anchor="middle" transform="translate(479 52) rotate(45)" dy="7">Get Details</text>
    </svg>
  </section>

  <section class="banner banner--square-b">
    <div class="photo" role="img" aria-label="Photo of a female operator wearing a headset in a dim command centre"></div>
    <div class="brand"><span class="brand__name">FieldKeepUnit</span><span class="brand__by">By Harrowmere</span></div>
    <h2 class="headline">Take Control<br>of Your Events</h2>
    <p class="tagline">Your Force Multiplier - Field Keep as a Service</p>
    <svg class="ribbon" viewBox="0 0 560 287" aria-hidden="true">
      <polygon points="418,0 476,0 560,84 560,142" fill="var(--ribbon-red)"/>
      <text x="0" y="0" font-size="19" text-anchor="middle" transform="translate(503 57) rotate(45)" dy="7">Get Details</text>
    </svg>
  </section>

  <section class="banner banner--wide">
    <div class="photo" role="img" aria-label="Photo of a female operator wearing a headset in a dim command centre"></div>
    <div class="brand"><span class="brand__name">FieldKeepUnit</span><span class="brand__by">By Harrowmere</span></div>
    <h2 class="headline">Take Control of Your Events</h2>
    <p class="tagline">Your Force Multiplier - Field Keep as a Service</p>
    <svg class="ribbon" viewBox="0 0 1138 145" aria-hidden="true">
      <polygon points="990,0 1048,0 1138,90 1138,145 1135,145" fill="var(--ribbon-red)"/>
      <text x="0" y="0" font-size="19" text-anchor="middle" transform="translate(1072 56) rotate(45)" dy="7">Get Details</text>
    </svg>
  </section>

</main>
</body>
</html>
```